Modern two-sided business card for a general enterprise that improves the digital user experience.

Our company based in Switzerland covers all services of the digital customer relationship. We automate online ads to acquire new customers and program mobile apps for more efficient customer care in customer service. We employ specialists in marketing, business management, data science, graphic designers, copywriters, UI and programmers. The new business card is intended to show our comprehensive role and various offering of the entire customer journey.

Company Font: Futura
Main Color: # 283583
Secondary: #fcfaee (and gray variations)
Website: https://vko.example

As little address information as possible: company name, employee, mobile, email, company web & company phone.

Target Market(s)

C-Level (CEO, CIO, CTO), Head Sales, Head Marketing & Head Customer Service

Industry/Entity Type

Digital Marketing, Online-Marketing, Analytics

Contact Information for Business Card

Requirements
Must have
• Company logo type ": vko" only on one side

```html
<!DOCTYPE html>
<html lang="en">
<head>
<meta charset="utf-8">
<title>vko business card</title>
<link rel="stylesheet" href="https://fonts.googleapis.com/css2?family=Jost:wght@400;500;600&display=swap">
<style>
  :root {
    --brand-blue: #283583;
    --brand-blue-light: #34449a;
    --ink: #1c1c1e;
    --ink-muted: #3a3a3e;
    --card-white: #f2f2f2;
    --page-bg: #e4e4e6;
    --line-light: rgba(255, 255, 255, 0.75);
  }
  * { box-sizing: border-box; margin: 0; padding: 0; }
  html, body {
    width: 1200px; height: 944px; overflow: hidden;
    background: var(--page-bg);
    font-family: "Jost", "Futura", sans-serif;
  }
  .canvas {
    width: 1200px; height: 944px;
    display: flex; align-items: center; justify-content: center; gap: 40px;
  }
  .card {
    position: relative;
    width: 540px; height: 349px;
    overflow: hidden;
    box-shadow: 0 10px 30px rgba(0,0,0,0.12);
  }

  /* Services side */
  .card--services { background: var(--brand-blue); color: #fff; }
  .services-texture {
    position: absolute; left: 0; right: 0; top: 0; height: 62%;
    background: linear-gradient(200deg, var(--brand-blue-light) 0%, rgba(52,68,154,0.55) 45%, rgba(40,53,131,0) 100%);
  }
  .services-block {
    position: absolute; left: 48px; right: 48px; bottom: 50px;
  }
  .services-rule { height: 1px; background: var(--line-light); }
  .services-rule--top { width: 62%; margin-left: 38%; margin-bottom: 20px; }
  .services-title {
    font-weight: 500; font-size: 24px; letter-spacing: 0.06em;
    text-transform: uppercase; margin-bottom: 8px;
  }
  .services-rule--bottom { margin-bottom: 12px; width: 100%; }
  .services-list { list-style: none; font-size: 15.5px; line-height: 1.55; letter-spacing: 0.03em; }

  /* Contact side */
  .card--contact { background: var(--card-white); color: var(--ink); }
  .wordmark {
    position: absolute; top: 34px; right: 42px;
    color: var(--ink); font-weight: 600; font-size: 56px; line-height: 1; letter-spacing: 0.02em;
  }
  .divider { position: absolute; height: 1px; background: var(--brand-blue); }
  .divider--main { left: 40px; right: 40px; top: 150px; }
  .person { position: absolute; left: 40px; top: 176px; }
  .person-name { color: var(--brand-blue); font-weight: 600; font-size: 24px; letter-spacing: 0.02em; line-height: 1.25; }
  .person-role { color: var(--ink-muted); font-size: 15px; letter-spacing: 0.03em; line-height: 1.5; }
  .divider--contact { left: 40px; width: 170px; top: 238px; }
  .contact-list { position: absolute; left: 40px; top: 246px; list-style: none; font-size: 15px; color: var(--ink-muted); letter-spacing: 0.02em; }
  .contact-item { display: flex; align-items: center; gap: 10px; line-height: 1.45; }
  .contact-icon { width: 13px; height: 13px; fill: var(--brand-blue); flex: none; }
  .company { position: absolute; right: 40px; top: 262px; text-align right; text-align: right; }
  .company-name { color: var(--brand-blue); font-weight: 600; font-size: 16px; letter-spacing: 0.02em; }
  .company-address { color: var(--ink-muted); font-size: 14px; letter-spacing: 0.02em; }
  .bar { position: absolute; bottom: 0; height: 12px; }
  .bar--ink { left: 0; width: 64%; background: var(--ink); }
  .bar--blue { left: calc(64% + 6px); right: 0; background: var(--brand-blue); }
</style>
</head>
<body>
<main class="canvas">

  <section class="card card--services" aria-label="Card back: services">
    <div class="services-texture" role="img" aria-label="Faint dotted pattern in lighter blue across the upper card"></div>
    <div class="services-block">
      <div class="services-rule services-rule--top"></div>
      <h2 class="services-title">Our Services</h2>
      <div class="services-rule services-rule--bottom"></div>
      <ul class="services-list">
        <li>Specialists in marketing &nbsp;•&nbsp; Business management</li>
        <li>Data science &nbsp;•&nbsp; Copywriters &nbsp;•&nbsp; Graphic designers</li>
        <li>UI and programmers &nbsp;•&nbsp; Customer service apps</li>
      </ul>
    </div>
  </section>

  <section class="card card--contact" aria-label="Card front: contact">
    <p class="wordmark">vko</p>
    <div class="divider divider--main"></div>

    <div class="person">
      <h1 class="person-name">Mara Keller</h1>
      <p class="person-role">Managing Director</p>
    </div>
    <div class="divider divider--contact"></div>

    <ul class="contact-list">
      <li class="contact-item">
        <svg class="contact-icon" viewBox="0 0 24 24" aria-hidden="true"><path d="M6.6 10.8a15.1 15.1 0 0 0 6.6 6.6l2.2-2.2a1 1 0 0 1 1-.25 11.4 11.4 0 0 0 3.6.57 1 1 0 0 1 1 1V20a1 1 0 0 1-1 1A17 17 0 0 1 3 4a1 1 0 0 1 1-1h3.5a1 1 0 0 1 1 1c0 1.25.2 2.45.57 3.6a1 1 0 0 1-.25 1z"/></svg>
        <span>078 555 31 62</span>
      </li>
      <li class="contact-item">
        <svg class="contact-icon" viewBox="0 0 24 24" aria-hidden="true"><path d="M2 5h20v14H2z M2 5l10 8 10-8" fill="var(--brand-blue)" stroke="var(--card-white)" stroke-width="1.6"/></svg>
        <span>mara.keller@vko.example</span>
      </li>
      <li class="contact-item">
        <svg class="contact-icon" viewBox="0 0 24 24" aria-hidden="true"><circle cx="12" cy="12" r="10"/><path d="M2 12h20M12 2c3 3 3 17 0 20M12 2c-3 3-3 17 0 20" fill="none" stroke="var(--card-white)" stroke-width="1.4"/></svg>
        <span>https://vko.example</span>
      </li>
    </ul>

    <div class="company">
      <p class="company-name">Company Name LTD</p>
      <p class="company-address">Address will be here</p>
    </div>

    <div class="bar bar--ink"></div>
    <div class="bar bar--blue"></div>
  </section>

</main>
</body>
</html>
```